Staffing Company Website

We need a website for a new company based out of central California called "Harbor Field Staffing". We staff truck drivers for agriculture trucking businesses. We don't want a super corporate feel, we want something that feels more inviting to the kind of person who would work in Agriculture/Trucking while still being professional. Please let me know if you have any questions

```html
<!DOCTYPE html>
<html lang="en">
<head>
<meta charset="utf-8">
<title>Harbor Field Staffing</title>
<link href="https://fonts.googleapis.com/css2?family=Archivo:wght@400;500;600;700;800&display=swap" rel="stylesheet">
<style>
:root{
  --bar:#c08a5a;
  --copper:#c7875a;
  --sand:#dca06a;
  --clay:#c98a5b;
  --rust:#b07548;
  --ink:#2b2b2b;
  --slate:#5c6670;
  --white:#ffffff;
  --line:#d9d9d9;
}
*{margin:0;padding:0;box-sizing:border-box}
html,body{width:1200px;height:1200px;overflow:hidden;background:var(--white);font-family:"Archivo",Arial,sans-serif;color:var(--ink)}
.page{position:relative;width:1200px;height:1200px}
.topbar{position:absolute;left:0;top:0;width:1200px;height:36px;background:var(--bar);display:flex;align-items:center;padding:0 18px;color:var(--white);font-size:11px;font-weight:600;letter-spacing:.3px;text-transform:uppercase}
.topbar .social{margin-left:auto;display:flex;gap:10px;align-items:center}
.topbar .dot{width:26px;height:26px;border-radius:50%;background:#a8744a}
.topbar .dot.dark{background:#3a3f47}
.topbar .apply{margin-left:4px;background:var(--white);color:var(--ink);border-radius:14px;padding:6px 16px;font-size:10px;text-transform:none}
.header{position:absolute;top:36px;left:0;width:1200px;height:80px;display:flex;align-items:center;padding:0 20px;border-bottom:1px solid #eee}
.brand{display:flex;align-items:center;gap:12px}
.brand .mark{width:44px;height:44px;border-radius:50%;background:var(--copper)}
.brand .name{font-size:26px;font-weight:800;color:var(--ink)}
.nav{margin-left:auto;display:flex;gap:38px;font-size:13px;font-weight:600;text-transform:uppercase}
.nav a{color:var(--ink);text-decoration:none}
.nav a.active{color:var(--copper)}
.hero{position:absolute;top:116px;left:0;width:1200px;height:472px;background:linear-gradient(180deg,#9a9aa2 0%,#c7a99a 45%,#d9a27a 60%,#8f8a6c 80%,#5e6a4c 100%)}
.hero-title{position:absolute;left:370px;top:122px;color:var(--white);font-size:60px;font-weight:700;line-height:62px;text-shadow:0 2px 6px rgba(0,0,0,.35)}
.hero-sub{position:absolute;left:390px;top:248px;color:var(--white);font-size:13px}
.cards{position:absolute;top:588px;left:0;width:1200px;height:169px;display:flex}
.card{flex:1;color:var(--white);text-align:center;padding-top:26px}
.card:nth-child(1){background:var(--copper)}
.card:nth-child(2){background:var(--sand)}
.card:nth-child(3){background:var(--clay)}
.card:nth-child(4){background:var(--rust)}
.card svg{display:block;margin:0 auto 10px}
.card h3{font-size:17px;font-weight:600;margin-bottom:10px}
.card p{font-size:12px;line-height:16px;padding:0 40px;opacity:.92}
.feature{position:absolute;left:0;top:770px;width:594px;height:430px;background:linear-gradient(180deg,#4c5562 0%,#6c6a68 45%,#7a5338 75%,#9a8460 100%)}
.feature h2{position:absolute;left:26px;top:80px;color:var(--white);font-size:35px;font-weight:800}
.feature p{position:absolute;left:24px;top:140px;width:500px;color:var(--white);font-size:15px;line-height:22px}
.btn{display:inline-block;background:var(--copper);color:var(--white);font-weight:600;font-size:14px;text-align:center;border-radius:24px}
.feature .btn{position:absolute;left:23px;top:278px;width:226px;height:48px;line-height:48px}
.about{position:absolute;left:606px;top:770px;width:293px;height:430px;background:linear-gradient(180deg,#6f7a86 0%,#9aa0a6 55%,#3b3f44 85%,#2e3136 100%);color:var(--white)}
.about h2{text-align:center;font-size:28px;font-weight:700;margin-top:57px}
.about .rule{margin:12px auto 0;width:250px;height:3px;background:var(--white)}
.about ul{list-style:none;margin:20px 22px 0}
.about li{display:flex;align-items:center;gap:10px;height:50px;border-top:1px solid rgba(255,255,255,.45);font-size:14px;font-weight:600}
.about li:last-child{border-bottom:1px solid rgba(255,255,255,.45)}
.about .foot{position:absolute;left:0;bottom:60px;width:100%;text-align:center;font-size:13px;font-weight:600}
.about .foot:before{content:"";display:block;width:260px;height:3px;background:var(--white);margin:0 auto 26px}
.services{position:absolute;left:920px;top:770px;width:260px;height:430px}
.services h2{font-size:26px;font-weight:700;margin-top:48px}
.services .rule{margin-top:14px;height:2px;background:var(--copper)}
.field{border:1px solid var(--line);border-radius:12px;height:44px;padding:0 12px;display:flex;align-items:center;font-size:14px;font-weight:600;margin-top:14px}
.field.msg{height:82px;align-items:flex-start;padding-top:12px;color:var(--copper);font-size:12px}
.services .btn{display:block;margin-top:18px;height:46px;line-height:46px;font-size:15px}
</style>
</head>
<body>
<div class="page">
  <div class="topbar">
    <span>Now hiring drivers across the Central Valley</span>
    <div class="social"><span class="dot"></span><span class="dot dark"></span><span class="apply">Apply today</span></div>
  </div>
  <header class="header">
    <div class="brand"><span class="mark"></span><span class="name">Harbor Field Staffing</span></div>
    <nav class="nav">
      <a class="active" href="#">About</a><a href="#">Drivers</a><a href="#">Services</a><a href="#">Clients</a><a href="#">Careers</a><a href="#">Contact</a>
    </nav>
  </header>
  <section class="hero" role="img" aria-label="Photo of white semi trucks hauling farm loads across a field at sunset">
    <h1 class="hero-title">Harbor Field<br>Staffing</h1>
    <p class="hero-sub">Drivers for the farms that feed us</p>
  </section>
  <section class="cards">
    <div class="card">
      <svg width="28" height="26" viewBox="0 0 28 26" fill="none" stroke="#fff" stroke-width="2"><rect x="2" y="2" width="24" height="16" rx="2"/><path d="M9 24h10M14 18v6"/></svg>
      <h3>Central California</h3><p>Local drivers who know the valley roads.</p>
    </div>
    <div class="card">
      <svg width="28" height="26" viewBox="0 0 28 26" fill="none" stroke="#fff" stroke-width="2"><rect x="2" y="2" width="24" height="16" rx="2"/><path d="M9 24h10M14 18v6"/></svg>
      <h3>Agri Trucking Staffing</h3><p>Seasonal and year-round haulers for every harvest.</p>
    </div>
    <div class="card">
      <svg width="28" height="26" viewBox="0 0 28 26" fill="none" stroke="#fff" stroke-width="2"><rect x="2" y="2" width="24" height="16" rx="2"/><path d="M9 24h10M14 18v6"/></svg>
      <h3>Staffing Recruiting</h3><p>We screen, place and support every driver we staff.</p>
    </div>
    <div class="card">
      <svg width="28" height="26" viewBox="0 0 28 26" fill="none" stroke="#fff" stroke-width="2"><rect x="2" y="2" width="24" height="16" rx="2"/><path d="M9 24h10M14 18v6"/></svg>
      <h3>Contracts for Staffing</h3><p>Flexible crews for growers and carriers.</p>
    </div>
  </section>
  <section class="feature" role="img" aria-label="Photo of a rusty dump truck on a farm road under a dusky sky">
    <h2>SMALL TRUCK HAULERS</h2>
    <p>Harbor Field Staffing matches truck drivers with agriculture haulers across the valley. We know the work, the seasons and the roads, and we treat every driver like a neighbor. Find steady work close to home, with people who respect the job.</p>
    <a class="btn" href="#">FIND YOUR ROUTE</a>
  </section>
  <section class="about" role="img" aria-label="Photo of a truck on a dusty road at dusk">
    <h2>ABOUT</h2>
    <div class="rule"></div>
    <ul>
      <li><svg width="22" height="22" viewBox="0 0 22 22" fill="none" stroke="#fff" stroke-width="1.6"><circle cx="11" cy="11" r="9.5"/><path d="M7 11l3 3 5-6"/></svg>TRUCKING</li>
      <li><svg width="22" height="22" viewBox="0 0 22 22" fill="none" stroke="#fff" stroke-width="1.6"><circle cx="11" cy="11" r="9.5"/><path d="M7 11l3 3 5-6"/></svg>OUR ONE-STOP SERVICE</li>
      <li><svg width="22" height="22" viewBox="0 0 22 22" fill="none" stroke="#fff" stroke-width="1.6"><circle cx="11" cy="11" r="9.5"/><path d="M7 11l3 3 5-6"/></svg>THE CREW ROSTER</li>
    </ul>
    <div class="foot">VALUE DRIVERS</div>
  </section>
  <section class="services">
    <h2>SERVICES</h2>
    <div class="rule"></div>
    <div class="field">SERVICE</div>
    <div class="field">DRIVER SELECT</div>
    <div class="field msg">YOUR MESSAGE</div>
    <a class="btn" href="#">CONTACT</a>
  </section>
</div>
</body>
</html>
```